Harborline Estates Business Card for Apartment Buildings

Create business cards for resident managers who run apartment buildings. The audience is the public who are searching for apartment rentals, and current residents who live at the apartment building. Key design element will be incorporating the company logo, however, the logo cannot dominate. The building name and manager name are more important than the logo. Current business card design leaves little room for copy, so we may need to reduce the size on the current card to allow for more space for copy.

Target Market(s)

Adults 18-65 years of age, who are looking for an apartment rental, plus current residents who live at our apartment buildings.

Industry/Entity Type

Property Management

Contact Information for Business Card

A major design element will be use of the company logo. Important property and manager contact information must be part of the design. The size of the logo will need to be reduced to make room for building and manager contact copy.

Font styles to use
Sans Serif

Colors
3176b5
000000
959595
ffffff

Requirements
Must have
• 1) Incorporate the company logo.
• 2) Use the company colors (dark blue, black/grey, over white).
• 3) FEATURE THE BUILDING NAME
• 4) FEATURE THE MANAGER NAME
• 5) The company name is less important than BUILDING and MANAGER
• 6) Manager contact information
• **SEE ATTACHED CREATIVE BRIEF**
Nice to have
• 1) Back of card logo watermark
• 2) Ability to write notes on back of carfd
Should not have
• Avoid letting the company logo dominate the card, the building name and manager are more important than the company logo.

```html
<!DOCTYPE html>
<html lang="en">
<head>
<meta charset="utf-8">
<title>Harborline Estates – Business Card</title>
<link rel="stylesheet" href="https://fonts.googleapis.com/css2?family=Open+Sans:wght@400;600;700&display=swap">
<style>
  :root {
    --brand-blue: #1f6dab;
    --ink: #2b2b2b;
    --card: #ececec;
    --backdrop: #e6e2dc;
    --shadow: rgba(0, 0, 0, 0.35);
  }
  html, body {
    margin: 0;
    width: 1200px;
    height: 900px;
    overflow: hidden;
    background: var(--backdrop);
    font-family: "Open Sans", Arial, sans-serif;
  }
  .stage { position: relative; width: 1200px; height: 900px; }
  .card {
    position: absolute;
    background: var(--card);
    box-shadow: 2px 3px 6px var(--shadow);
    overflow: hidden;
  }
  .card--front { left: 320px; top: 87px; width: 580px; height: 358px; }
  .card--back  { left: 320px; top: 478px; width: 583px; height: 359px; }

  .brand {
    position: absolute;
    left: 126px; top: 42px;
    display: flex; align-items: center; gap: 16px;
    color: var(--brand-blue);
    font-weight: 700;
  }
  .brand__mark { width: 56px; height: 56px; background: var(--brand-blue); }
  .brand__name { line-height: 1; }
  .brand__line1 { display: block; font-size: 44px; letter-spacing: 0.5px; }
  .brand__line2 { display: block; font-size: 21px; letter-spacing: 4.2px; margin-top: 6px; }

  .person { position: absolute; left: 0; right: 0; top: 150px; text-align: center; }
  .person__name { margin: 0; font-size: 20px; font-weight: 700; color: var(--ink); line-height: 1.2; }
  .person__first { color: var(--brand-blue); }
  .person__role { margin: 2px 0 0; font-size: 15px; color: var(--ink); }

  .contact {
    position: absolute; left: 0; right: 0; top: 215px;
    list-style: none; margin: 0; padding: 0;
    text-align: center; font-size: 15px; color: var(--ink);
  }
  .contact li { height: 21px; line-height: 21px; }
  .contact svg { width: 13px; height: 13px; vertical-align: -1px; margin-right: 4px; fill: var(--brand-blue); }
  .address {
    position: absolute; left: 0; right: 0; top: 307px;
    margin: 0; text-align: center; font-size: 15px; color: var(--ink);
  }

  /* Back: large plain square bleeding off the left edge, name set beside it */
  .back__block {
    position: absolute;
    left: -222px; top: 0;
    width: 359px; height: 359px;
    background: var(--ink);
  }
  .back__name {
    position: absolute;
    left: 172px; top: 30px;
    margin: 0;
    font-size: 34px; font-weight: 700; line-height: 1.1;
    color: var(--brand-blue);
  }
</style>
</head>
<body>
<main class="stage">
  <section class="card card--front" aria-label="Business card front">
    <div class="brand">
      <span class="brand__mark" aria-hidden="true"></span>
      <span class="brand__name">
        <span class="brand__line1">HARBORLINE</span>
        <span class="brand__line2">ESTATES LLC</span>
      </span>
    </div>

    <div class="person">
      <h1 class="person__name"><span class="person__first">DANIEL</span> REYES</h1>
      <p class="person__role">Property Manage</p>
    </div>

    <ul class="contact">
      <li><svg viewBox="0 0 16 16" aria-hidden="true"><path d="M2 5c0-2 2-3 6-3s6 1 6 3v1h-3V5H5v1H2zM4 7h8l2 6H2z"/></svg>555-014-2276</li>
      <li><svg viewBox="0 0 16 16" aria-hidden="true"><path d="M5 1h7v4H5zM1 5h3v10H1zM5 6h10v9H5zm2 2v2h6V8z"/></svg>555-014-8830</li>
      <li><svg viewBox="0 0 16 16" aria-hidden="true"><path d="M1 3h14v10H1zm1 1v1l6 4 6-4V4z"/></svg>daniel@harborlineestates.us</li>
      <li><svg viewBox="0 0 16 16" aria-hidden="true"><circle cx="8" cy="8" r="7"/></svg>www.harborlineestates.us</li>
    </ul>

    <p class="address">2170 Alder Grove Road #B210 Fairview, Ca 90000</p>
  </section>

  <section class="card card--back" aria-label="Business card back">
    <span class="back__block" aria-hidden="true"></span>
    <p class="back__name">Harborline Estates</p>
  </section>
</main>
</body>
</html>
```